Website for a web design agency

We are a website and marketing agency. We do website design, development, and well as Quorvel and Pinglet advertising and analytics. We ourselves need a new website for our own brand. We are working on some designs in-house with our own designers, but we also wanted to see what outside designers would come up with.
We are starting off with the homepage, and here is the breakdown of the sections:
https://docs.quorvel-sample.com/document/d/7hkW2mPqRtLxZ9vBnC4sYeJ8uDfGaTo1Ni3QwEr6KbUz/edit?usp=sharing
This doc also has many links to sites we have done, which you can take screenshots of for the portfolio section.
In terms of the "look" I am going for, I want to look high-end and very beautiful designs. I found this website that I like a lot that you can use some of the elements of, just as a starting point:
http://brindlecove-sample.com/themes/pixelbazaar/html/toverin/index.html and here is another design option they have http://brindlecove-sample.com/themes/pixelbazaar/html/toverin/index-4.html
I'm also uploading my logo. The logo matches the gold and black look from these websites, but I would be open to switching to another color scheme if needed.
This is the link to my very old website, which you can use for some of the dummy text, and a pic of myself. I will be taking more pics of myself:
https://thewindyorchardpathstudio-sample.com/
We need a homepage and a portfolio page right now, but if you are the winner, we will be hiring you to make additional pages.
Updates
More designs continue to come in even today, and I want to make sure no other designers are still submitting designs.
Target Market(s)
medium and large businesses owners, and non-profits
Number of Pages Required
1 page

```html
<!DOCTYPE html>
<html lang="en">
<head>
<meta charset="utf-8">
<title>Norvane Strategies — Home</title>
<link rel="stylesheet" href="https://fonts.googleapis.com/css2?family=Oswald:wght@400;500&family=Montserrat:wght@400;500;600;700&family=Open+Sans:wght@400;600;700&display=swap">
<style>
:root{
  --green:#35a57c;
  --green-soft:#d7efe5;
  --ink:#111216;
  --dark:#17191e;
  --text:#222;
  --muted:#8c8c8c;
  --white:#fff;
  --page:#f0f1f1;
}
*{box-sizing:border-box;margin:0;padding:0}
html,body{width:1200px;height:3000px;overflow:hidden;background:var(--page)}
body{position:relative;font-family:'Open Sans',sans-serif;color:var(--text)}
.site{position:absolute;left:195px;top:36px;width:810px;height:2929px;background:var(--white);box-shadow:0 10px 40px rgba(0,0,0,.12);overflow:hidden}
section,header,nav,footer{position:absolute;left:0;width:810px;overflow:hidden}
.abs{position:absolute}
.green{color:var(--green)}
.heading{font-family:'Oswald',sans-serif;font-weight:500;text-transform:uppercase;text-align:center;width:100%;letter-spacing:.5px}
.btn{position:absolute;background:var(--green);color:#fff;font-family:'Montserrat',sans-serif;font-weight:600;font-size:9px;border-radius:16px;display:flex;align-items:center;justify-content:center;letter-spacing:.3px;box-shadow:0 3px 6px rgba(0,0,0,.18)}

/* top bar */
.topbar{top:0;height:21px;background:var(--ink);color:#ddd;font-size:7px}
.topbar .item{position:absolute;top:0;height:21px;display:flex;align-items:center;gap:6px;white-space:nowrap}
.social{display:flex;gap:9px}
.social span{width:10px;height:10px;border-radius:50%;border:1.4px solid #eee;display:block}

/* nav */
.nav{top:21px;height:38px;background:var(--green)}
.brand{position:absolute;font-family:'Montserrat',sans-serif;font-weight:700;color:#fff;line-height:1}
.brand .name{font-size:16px;letter-spacing:1px}
.brand .tag{font-size:6px;letter-spacing:3.2px;font-weight:500}
.nav .links{position:absolute;left:0;top:0;width:810px;height:38px;font-family:'Montserrat',sans-serif;font-size:9px;color:#fff}
.nav .links a{position:absolute;top:14px;white-space:nowrap;line-height:10px}
.nav .cta{position:absolute;left:675px;top:5px;width:102px;height:28px;background:#fff;border-radius:15px;color:#111;font-family:'Montserrat',sans-serif;font-size:9px;font-weight:600;display:flex;align-items:center;justify-content:center}

/* hero */
.hero{top:59px;height:428px;background:linear-gradient(110deg,#3a3c3d 0%,#4d4f4f 45%,#6b6c6a 70%,#8a8b87 100%)}
.hero .photo{position:absolute;left:390px;top:0;width:420px;height:428px;background:radial-gradient(ellipse at 50% 35%,#9b8e84 0%,#74706b 40%,rgba(80,80,80,0) 75%)}
.hero h1{position:absolute;left:41px;top:153px;font-family:'Oswald',sans-serif;font-weight:400;font-size:48px;line-height:50px;color:#fff;letter-spacing:-.3px}
.hero .sub{position:absolute;left:47px;top:212px;font-family:'Montserrat',sans-serif;font-weight:500;font-size:19px;line-height:30px;color:#fff}
.hero .ghost{position:absolute;left:47px;top:285px;width:115px;height:30px;border:2px solid var(--green);border-radius:16px;color:#fff;font-family:'Montserrat',sans-serif;font-size:8px;font-weight:600;display:flex;align-items:center;justify-content:center}
.hero .play{position:absolute;left:178px;top:284px;width:32px;height:32px;border-radius:50%;background:#e9e9e9}

/* about */
.about{top:487px;height:393px;background:#fff}
.about .net{position:absolute;left:0;top:230px;width:810px;height:163px;background:linear-gradient(180deg,rgba(255,255,255,0) 0%,rgba(198,232,219,.45) 60%,rgba(198,232,219,.6) 100%)}
.about h2{position:absolute;top:46px;font-size:30px;color:var(--ink)}
.about p{position:absolute;left:127px;width:556px;text-align:center;font-size:9.2px;line-height:13.5px;font-weight:600}
.about p.lead{color:var(--green);font-weight:400}

/* what we do */
.services{top:880px;height:391px;background:linear-gradient(120deg,#0f1014 0%,#1b1d25 45%,#2a1a22 75%,#14151b 100%)}
.services .code{position:absolute;inset:0;background:linear-gradient(160deg,rgba(120,30,40,.25) 0%,rgba(40,40,60,.1) 50%,rgba(60,90,130,.18) 100%)}
.services h2{position:absolute;top:26px;font-size:30px;color:#fff}
.services .intro{position:absolute;top:80px;left:100px;width:610px;text-align:center;color:#fff;font-size:9.5px;line-height:14px;font-family:'Montserrat',sans-serif;font-weight:500}
.pill{position:absolute;width:202px;height:54px;border:1.5px solid var(--green);border-radius:28px;font-size:6.3px;line-height:8px;color:#ddd}
.pill .t{color:var(--green);font-family:'Montserrat',sans-serif;font-weight:600;font-size:7px;text-transform:uppercase;margin-bottom:2px}
.pill.left{text-align:right;padding:10px 66px 0 14px}
.pill.right{text-align:left;padding:10px 14px 0 64px}

/* portfolio */
.portfolio{top:1271px;height:543px;background:#fff}
.portfolio h2{position:absolute;top:50px;font-size:30px;color:var(--ink)}
.shot{position:absolute;box-shadow:0 2px 6px rgba(0,0,0,.12)}

/* testimonials */
.testimonials{top:1814px;height:320px;background:linear-gradient(115deg,#2b2e33 0%,#3a3d40 35%,#2c2f33 65%,#1d1f23 100%)}
.testimonials h2{position:absolute;top:40px;font-family:'Oswald',sans-serif;font-weight:500;font-size:40px;width:100%;text-align:center;color:#fff}
.avatar{position:absolute;border-radius:50%;border:2px solid #fff}
.testimonials .quote{position:absolute;left:110px;top:181px;width:590px;text-align:center;color:#fff;font-size:10px;line-height:20px}
.testimonials .name{position:absolute;top:260px;width:100%;text-align:center;color:var(--green);font-family:'Montserrat',sans-serif;font-weight:600;font-size:11px;text-decoration:underline}

/* news */
.news{top:2134px;height:558px;background:#fff}
.news h2{position:absolute;top:72px;width:100%;text-align:center;font-family:'Oswald',sans-serif;font-weight:500;font-size:40px;color:var(--ink)}
.card{position:absolute;width:181px}
.card .img{height:88px}
.card .meta{margin-top:19px;font-size:7px;color:var(--muted)}
.card h3{margin-top:10px;font-family:'Montserrat',sans-serif;font-weight:700;font-size:12px;line-height:19px;color:#111}
.card p{margin-top:4px;font-size:8.4px;line-height:15px;color:#333}
.card .more{margin-top:6px;font-family:'Montserrat',sans-serif;font-weight:700;font-size:9.5px;color:#111}
.news .featured{position:absolute;left:298px;top:158px;width:214px;height:254px;background:#fff;box-shadow:0 4px 20px rgba(0,0,0,.12)}

/* footer */
.footer{top:2692px;height:237px;background:linear-gradient(120deg,#1f2226 0%,#2a2d31 50%,#171a1d 100%);color:#fff}
.footer h4{position:absolute;top:48px;font-family:'Montserrat',sans-serif;font-weight:500;font-size:13px;letter-spacing:.3px}
.footer ul{position:absolute;list-style:none;font-size:9px}
.footer li{position:relative;padding-left:22px}
.footer li::before{content:"";position:absolute;left:0;top:4px;width:5px;height:5px;border-radius:50%;background:#fff}
.footer .about-text{position:absolute;left:50px;top:88px;width:190px;font-size:8.4px;line-height:15px}
.footer .copy{position:absolute;top:225px;width:100%;text-align:center;font-size:8.5px;color:#eee}
</style>
</head>
<body>
<div class="site">

  <header class="topbar">
    <div class="item" style="left:50px">
      <svg width="12" height="9" viewBox="0 0 12 9"><rect x=".5" y=".5" width="11" height="8" fill="none" stroke="#eee"/><path d="M.5.5 6 5l5.5-4.5" fill="none" stroke="#eee"/></svg>
      <span>norvanestrategies.com</span>
    </div>
    <div class="item" style="left:362px">
      <svg width="9" height="11" viewBox="0 0 9 11"><path d="M2 0 4 3 3 4.5c.6 1.4 1.6 2.5 3 3.2L7 6.6l2 2L8 10.5C4 10.2.6 6 0 1.5Z" fill="#eee"/></svg>
      <span>555-014-2287</span>
    </div>
    <div class="item social" style="left:685px"><span></span><span></span><span></span><span></span></div>
  </header>

  <nav class="nav">
    <div class="brand" style="left:52px;top:8px"><div class="name">NORVANE</div><div class="tag">STRATEGIES</div></div>
    <div class="links">
      <a style="left:259px">Home</a>
      <a style="left:306px">what we do</a>
      <a style="left:376px">Portfolio</a>
      <a style="left:433px">Testimonials</a>
      <a style="left:508px">Our Team</a>
    </div>
    <div class="cta">CONTACT US</div>
  </nav>

  <section class="hero">
    <div class="photo" role="img" aria-label="Portrait photo of the agency founder against a grey wall"></div>
    <h1>We <span class="green">Build</span> Value</h1>
    <div class="sub">Enterprise Level Website Development<br>And Online Marketing</div>
    <div class="ghost">SEE HOW WE DO IT</div>
    <div class="play"><svg width="32" height="32" viewBox="0 0 32 32"><path d="M13 10v12l10-6z" fill="var(--green)"/></svg></div>
  </section>

  <section class="about">
    <div class="net" role="img" aria-label="Soft green network pattern of joined dots"></div>
    <h2 class="heading">About <span class="green">Norvane</span></h2>
    <p class="lead" style="top:114px">lorem ipsum dolor sit amet, consectetur adipiscing elit. at praesent ac eget commodo eget sed convallis. feugiat porta erat quis tellus purus cras ante tellus velit.</p>
    <p style="top:154px">Lorem ipsum dolor sit amet, consectetur adipiscing elit. Elit nunc nullam urna morbi tincidunt vitae sit rutrum. Laoreet ut ut convallis mi ut tortor sed pellentesque aliquam. Amet, posuere justo et amet tellus, non. Maecenas nunc euismod nunc id turpis. Mauris, nunc suspendisse turpis nunc nibh nullam. Dictum volutpat auctor nisl enim, urna mauris tempor eu et.</p>
    <p style="top:211px">Lorem ipsum dolor sit amet, consectetur adipiscing elit. Elit nunc nullam urna morbi tincidunt vitae sit rutrum. Laoreet ut ut convallis mi ut tortor sed pellentesque aliquam. Amet, posuere justo et amet tellus, non. Maecenas nunc euismod nunc id turpis. Mauris, nunc suspendisse turpis nunc nibh nullam. Dictum volutpat auctor nisl enim, urna mauris tempor eu et.</p>
    <p class="lead" style="top:268px">Lorem ipsum dolor sit amet, consectetur adipiscing elit. At praesent ac eget commodo eget sed convallis. Feugiat porta erat quis tellus purus cras ante tellus velit.</p>
    <div class="btn" style="left:349px;top:310px;width:111px;height:28px">LEARN MORE</div>
  </section>

  <section class="services">
    <div class="code" role="img" aria-label="Blurred screen of source code in red and blue tones"></div>
    <h2 class="heading">What <span class="green">We Do</span></h2>
    <div class="intro">Lorem ipsum dolor sit amet, consectetur adipiscing elit. Elit nunc nullam urna morbi tincidunt vitae sit rutrum.<br>Laoreet ut ut convallis mi ut tortor sed pellentesque aliquam.</div>
    <svg class="abs" style="left:0;top:0" width="810" height="391" viewBox="0 0 810 391">
      <g stroke="#e8e8e8" stroke-width="1" fill="none">
        <path d="M291 161 363 193M291 232 357 232M291 304 363 271M519 161 447 193M519 232 453 232M519 304 447 271"/>
      </g>
      <circle cx="405" cy="232" r="47" fill="#15171c" stroke="var(--green)" stroke-width="2"/>
      <circle cx="405" cy="232" r="40" fill="none" stroke="var(--green)" stroke-width="1"/>
      <g fill="#fff"><circle cx="363" cy="193" r="3.5"/><circle cx="357" cy="232" r="3.5"/><circle cx="363" cy="271" r="3.5"/><circle cx="447" cy="193" r="3.5"/><circle cx="453" cy="232" r="3.5"/><circle cx="447" cy="271" r="3.5"/></g>
      <text x="405" y="233" text-anchor="middle" font-family="Montserrat,sans-serif" font-weight="700" font-size="13" fill="#fff">NORVANE</text>
      <text x="405" y="243" text-anchor="middle" font-family="Montserrat,sans-serif" font-size="5" letter-spacing="2" fill="#fff">STRATEGIES</text>
    </svg>
    <div class="pill left" style="left:92px;top:134px"><div class="t">Landing Page</div>Lorem ipsum dolor sit amet, consectetur adipiscing elit. Elit id at quis ut. Potenti enim semper eu morbi elit ipsum.</div>
    <div class="pill left" style="left:92px;top:205px"><div class="t">Donation Pages</div>Lorem ipsum dolor sit amet, consectetur adipiscing elit. Elit id at quis ut. Potenti enim semper eu morbi elit ipsum.</div>
    <div class="pill left" style="left:92px;top:277px"><div class="t">Donation Pages</div>Lorem ipsum dolor sit amet, consectetur adipiscing elit. Elit id at quis ut. Potenti enim semper eu morbi elit ipsum.</div>
    <div class="pill right" style="left:516px;top:134px"><div class="t">Website Design</div>Lorem ipsum dolor sit amet, consectetur adipiscing elit. Elit id at quis ut. Potenti enim semper eu morbi elit ipsum.</div>
    <div class="pill right" style="left:516px;top:205px"><div class="t">Analytics and Optimization</div>Lorem ipsum dolor sit amet, consectetur adipiscing elit. Elit id at quis ut. Potenti enim semper eu morbi elit ipsum.</div>
    <div class="pill right" style="left:516px;top:277px"><div class="t">Video Marketing</div>Lorem ipsum dolor sit amet, consectetur adipiscing elit. Elit id at quis ut. Potenti enim semper eu morbi elit ipsum.</div>
    <svg class="abs" style="left:0;top:0" width="810" height="391" viewBox="0 0 810 391">
      <g fill="#fff" stroke="var(--green)" stroke-width="2">
        <circle cx="267" cy="161" r="23"/><circle cx="267" cy="232" r="23"/><circle cx="267" cy="304" r="23"/>
        <circle cx="544" cy="161" r="23"/><circle cx="544" cy="232" r="23"/><circle cx="544" cy="304" r="23"/>
      </g>
      <g fill="none" stroke="#333" stroke-width="1.5">
        <rect x="257" y="151" width="20" height="15" rx="1"/><path d="M263 171h8M267 166v5"/>
        <circle cx="267" cy="230" r="7" fill="#f2c94c" stroke="#e0a92a"/>
        <rect x="257" y="295" width="20" height="14" rx="1"/><circle cx="267" cy="302" r="3.5"/>
        <rect x="534" y="152" width="20" height="17" rx="1"/><path d="M534 157h20"/>
        <rect x="535" y="224" width="16" height="13" rx="1"/><path d="M538 233l3-3 3 2 4-5"/>
        <rect x="534" y="296" width="8" height="7"/><rect x="546" y="296" width="8" height="7"/><rect x="540" y="306" width="8" height="7"/>
      </g>
      <g fill="#e24d4d"><circle cx="540" cy="163" r="1.6"/><circle cx="545" cy="163" r="1.6"/><circle cx="550" cy="163" r="1.6"/></g>
    </svg>
  </section>

  <section class="portfolio">
    <h2 class="heading">Our <span class="green">Portfolio</span></h2>
    <div class="shot" style="left:-5px;top:117px;width:46px;height:253px;background:linear-gradient(180deg,#f4d8d2 0%,#f0e9e6 25%,#8d8f97 40%,#ddd 60%,#c9c2b8 75%,#e9e6e6 100%)" role="img" aria-label="Partial website screenshot"></div>
    <div class="shot" style="left:70px;top:117px;width:131px;height:313px;background:linear-gradient(180deg,#7fa4c9 0%,#c7cfd6 18%,#f3f3f3 30%,#d7c9a6 42%,#6c7d52 52%,#a9c27c 62%,#f4f4f4 72%,#e7efe0 86%,#8fae5e 100%)" role="img" aria-label="Website screenshot of a nonprofit with landscape photos"></div>
    <div class="shot" style="left:214px;top:156px;width:147px;height:265px;background:linear-gradient(180deg,#f6dede 0%,#f2e3dd 30%,#4c3a6b 45%,#6b4c4e 55%,#ffffff 62%,#f4f0ec 72%,#8d7b6a 88%,#f2f2f2 100%)" role="img" aria-label="Website screenshots of a cosmetics shop and a nonprofit mission page"></div>
    <div class="shot" style="left:368px;top:141px;width:190px;height:92px;background:linear-gradient(120deg,#0f0f14 0%,#1c1d2b 50%,#2d6a8c 70%,#f28a2a 100%)" role="img" aria-label="Website screenshot of a dark media agency page"></div>
    <div class="shot" style="left:380px;top:257px;width:180px;height:158px;background:linear-gradient(180deg,#ffffff 0%,#f4f0e8 40%,#e9b94a 55%,#f6f6f6 75%,#f0f0f0 100%)" role="img" aria-label="Website screenshot of a comic book shop"></div>
    <div class="shot" style="left:573px;top:116px;width:151px;height:102px;background:linear-gradient(135deg,#2d3033 0%,#7a8088 50%,#3a3d40 100%)" role="img" aria-label="Website screenshot with video stills"></div>
    <div class="shot" style="left:573px;top:235px;width:151px;height:177px;background:linear-gradient(180deg,#f5f0f5 0%,#8a3b8c 20%,#5b3c7e 38%,#ffffff 55%,#7f5a9a 70%,#c58a5a 85%,#f2f2f2 100%)" role="img" aria-label="Website screenshot of a coaching brand in purple"></div>
    <div class="shot" style="left:752px;top:116px;width:70px;height:313px;background:linear-gradient(180deg,#7fa4c9 0%,#c7cfd6 18%,#f3f3f3 30%,#d7c9a6 42%,#6c7d52 52%,#a9c27c 62%,#f4f4f4 72%,#e7efe0 86%,#8fae5e 100%)" role="img" aria-label="Partial website screenshot"></div>
    <div class="btn" style="left:349px;top:466px;width:111px;height:29px">VIEW MORE</div>
  </section>

  <section class="testimonials">
    <div class="abs" style="inset:0;background:radial-gradient(ellipse at 30% 60%,rgba(90,95,100,.35),rgba(0,0,0,0) 60%)" role="img" aria-label="Dark photo of a team meeting around a table"></div>
    <h2>Testim<span class="green">onials</span></h2>
    <svg class="abs" style="left:244px;top:128px" width="32" height="12" viewBox="0 0 32 12"><path d="M31 6H2M7 1 1.5 6 7 11" fill="none" stroke="var(--green)" stroke-width="1.5"/></svg>
    <svg class="abs" style="left:535px;top:128px" width="32" height="12" viewBox="0 0 32 12"><path d="M1 6h29M25 1l5.5 5L25 11" fill="none" stroke="var(--green)" stroke-width="1.5"/></svg>
    <div class="avatar" style="left:318px;top:117px;width:34px;height:34px;background:#c9b3a6" role="img" aria-label="Client portrait"></div>
    <div class="avatar" style="left:346px;top:118px;width:33px;height:33px;background:#8e949a" role="img" aria-label="Client portrait"></div>
    <div class="avatar" style="left:383px;top:111px;width:48px;height:48px;background:#d8dde2;z-index:2" role="img" aria-label="Client portrait"></div>
    <div class="avatar" style="left:426px;top:118px;width:33px;height:33px;background:#7e8790" role="img" aria-label="Client portrait"></div>
    <div class="avatar" style="left:456px;top:118px;width:33px;height:33px;background:#c7b2a3" role="img" aria-label="Client portrait"></div>
    <div class="quote">Lorem Ipsum Dolor Sit Amet, Consectetur Adipiscing Elit. L Et Ut Amet. Et, Eget Phasellus Varius Cum. Sit Volutpat At Nec, Egestas Egestas. Cras Arcu, Fringilla Risus Volutpat Id Cursus Fringilla Laoreet FaucibusLorem Ipsum Dolor Sit Amet, Consectetur Adipiscing Elit. Luctus Quis Et Ut Amet. Et, Eget Phasellus</div>
    <div class="name">DARA LINWELL</div>
  </section>

  <section class="news">
    <h2>News/ <span class="green">Articles</span></h2>
    <div class="featured"></div>
    <article class="card" style="left:79px;top:169px">
      <div class="img" role="img" aria-label="Photo of a laptop on a desk" style="background:linear-gradient(135deg,#3a3b3f 0%,#8aa2c2 45%,#2a2b2e 100%)"></div>
      <div class="meta">By Admin, on Nov 23th, 2020 &nbsp;|&nbsp; 1 days ago</div>
      <h3>Lorem ipsum dolor sit amet, consectetur</h3>
      <p>Lorem ipsum dolor sit amet, consectetur adipiscing elit. Sed ac porttitor proin tempor, tortor ac.</p>
      <div class="more">Read more</div>
    </article>
    <article class="card" style="left:315px;top:169px">
      <div class="img" role="img" aria-label="Photo of a person working on a laptop" style="background:linear-gradient(135deg,#d8d4cf 0%,#6d6a66 45%,#c5bfb8 100%)"></div>
      <div class="meta">By Admin, on Nov 23th, 2020 &nbsp;|&nbsp; 1 days ago</div>
      <h3>Lorem ipsum dolor sit amet, consectetur</h3>
      <p>Lorem ipsum dolor sit amet, consectetur adipiscing elit. Sed ac porttitor proin tempor, tortor ac.</p>
      <div class="more">Read more</div>
    </article>
    <article class="card" style="left:550px;top:169px">
      <div class="img" role="img" aria-label="Photo of a bright desk with a monitor" style="background:linear-gradient(135deg,#eef0f2 0%,#b8c4d0 50%,#6c7580 100%)"></div>
      <div class="meta">By Admin, on Nov 23th, 2020 &nbsp;|&nbsp; 1 days ago</div>
      <h3>Lorem ipsum dolor sit amet, consectetur</h3>
      <p>Lorem ipsum dolor sit amet, consectetur adipiscing elit. Sed ac porttitor proin tempor, tortor ac.</p>
      <div class="more">Read more</div>
    </article>
    <div class="btn" style="left:360px;top:450px;width:112px;height:29px">READ MORE</div>
  </section>

  <footer class="footer">
    <div class="brand" style="left:48px;top:44px"><div class="name" style="font-size:22px">NORVANE</div><div class="tag" style="font-size:8px;letter-spacing:4.3px">STRATEGIES</div></div>
    <div class="about-text">Lorem ipsum dolor sit amet, consectetur adipiscing elit. Lacus augue nisl adipiscing accumsan suspendisse. Massa ipsum, sed lacus condimentum et ,Lorem ipsum dolor sit</div>
    <div class="abs social" style="left:50px;top:169px;gap:22px"><span></span><span></span><span></span><span></span></div>
    <h4 style="left:260px">QUICK LINKS</h4>
    <ul style="left:260px;top:82px;line-height:19.5px">
      <li>Home</li><li>What we do</li><li>Portfolio</li><li>Testimonials</li><li>Our Team</li>
    </ul>
    <h4 style="left:423px">RESOURCES</h4>
    <ul style="left:423px;top:83px;line-height:25px;font-size:8.5px">
      <li>Faq</li><li>Get A Quote</li><li>Treams &amp; Conditions</li><li>Privicy &amp; Terms</li>
    </ul>
    <h4 style="left:576px">OUR NEWSLETTER</h4>
    <div class="abs" style="left:576px;top:80px;font-size:7px">SUBSCRIBE OUR NEWSLETTER</div>
    <div class="abs" style="left:576px;top:110px;width:109px;height:21px;background:#fff;color:#777;font-size:6.5px;display:flex;align-items:center;padding-left:7px">ENTER YOUR EMAIL</div>
    <div class="abs" style="left:685px;top:110px;width:53px;height:21px;background:var(--green);color:#fff;font-size:6.5px;display:flex;align-items:center;justify-content:center">SUBMIT</div>
    <div class="abs" style="left:50px;top:218px;width:710px;height:1px;background:rgba(255,255,255,.2)"></div>
    <div class="copy">NORVANE STRATEGIES© 2021 All Rights Reserved. Terms of Use and Privacy Policy</div>
  </footer>

</div>
</body>
</html>
```